New Consulting Firm News PowerPoint Template

We are a new consulting firm that specializes in Veltrix Unified Planning Suite implementations in need of a new PowerPoint template. We need at least the following layouts:
• Main Cover Slide
• Agenda / Table of Contents
• Title slide for each of the agenda items leading into actual content
• Title + Content with nice bullets in the content
• Title + Sub-Title + Content with nice bullets in the content
• Title + Two Columns of Content
• Title + Sub-Title + Two Columns of Content
• Title + Three Columns of Content
• Title + Sub-Title + Three Columns of Content
• Title + Two Rows and Two Columns of Content (4 boxes)
• Title + Sub-Title + Two Rows and Two Columns of Content (4 boxes)
• Title + Blank
• Nascar Slide (Client logos arranged somehow)
• Case Study Slide
• Various infographic slides than can be used and modified would be amazing as well
Our logo has been uploaded and you can find our website here:
https://brannowadvisory.com
We would like the main theme colors to blend with our logo, but also have a variety of colors in the theme that compliment the main theme colors. Once we have selected a PowerPoint design we expect to immediately have a Word design contest and the winning PowerPoint design will likely be a heavy influence on the Word design.

Target Market(s)

CFO, CAO, VP of Finance, Controllers

Industry/Entity Type

Consulting

Font styles to use
Serif
Sans Serif

Requirements
Must have
• • Main Cover Slide
• Title + Blank
• Case Study Slide
Nice to have
• • Various infographic slides than can be used and modified would be amazing as well

```html
<!DOCTYPE html>
<html lang="en">
<head>
<meta charset="utf-8">
<title>Brannow Advisory – Presentation Template Sample Layout</title>
<link href="https://fonts.googleapis.com/css2?family=Bebas+Neue&family=Open+Sans:wght@400;600;700&display=swap" rel="stylesheet">
<style>
:root{
  --stage:#a7a9ac;
  --paper:#ffffff;
  --navy:#0d4a7a;
  --deep:#0b5c8c;
  --blue:#0a85c2;
  --sky:#3aa6d0;
  --ink:#222222;
  --grey:#6d6e71;
  --mist:#e8e8e8;
  --head:#0e6a94;
}
*{margin:0;padding:0;box-sizing:border-box}
html,body{width:1200px;height:900px;overflow:hidden;background:var(--paper)}
body{position:relative;font-family:"Open Sans",Arial,sans-serif}
.stage{position:absolute;left:0;top:0;width:1200px;height:556px;background:var(--stage)}
.slide{position:absolute;width:282px;height:159px;background:var(--paper);display:block}
.c1{left:16px}.c2{left:311px}.c3{left:607px}.c4{left:902px}
.r1{top:29px}.r2{top:201px}.r3{top:373px}
svg text{font-family:"Open Sans",Arial,sans-serif}
.title{font-size:15px;fill:var(--ink)}
.title .b{font-weight:700}
.title-w{font-size:15px;fill:#fff}
.title-w .b{font-weight:700}
.brand{font-size:10px;font-weight:700;fill:var(--blue);letter-spacing:.5px}
.brand-w{font-size:10px;font-weight:700;fill:#fff;letter-spacing:.5px}
.foot{font-size:6px;fill:var(--grey)}
.foot-w{font-size:6px;fill:#fff;font-weight:600}
.lab{font-size:7.5px;font-weight:700;fill:var(--ink)}
.lab-w{font-size:7.5px;font-weight:700;fill:#fff}
.fine{font-size:5.5px;fill:var(--grey)}
.fine-w{font-size:5.5px;fill:#fff}
.num{font-size:16px;fill:var(--ink)}
.copy{position:absolute;left:0;width:1200px;font-family:"Bebas Neue",Impact,sans-serif;color:var(--head);white-space:nowrap;line-height:1}
.headline{top:598px;font-size:52px;text-align:center}
.note{font-size:36px}
.n1{top:660px;left:213px}
.n2{top:705px;left:172px}
.n3{top:746px;left:172px}
.signoff{position:absolute;left:985px;top:722px;width:190px;text-align:center}
.signoff .mark{width:70px;height:70px;background:var(--blue);margin:0 auto 18px}
.signoff .name{font-family:"Open Sans",Arial,sans-serif;font-weight:600;color:var(--blue);font-size:34px;letter-spacing:2px;line-height:1}
.signoff .sub{font-family:"Open Sans",Arial,sans-serif;font-weight:600;color:var(--blue);font-size:13px;letter-spacing:4px;margin-top:4px}
</style>
</head>
<body>
<div class="stage"></div>

<!-- Cover -->
<svg class="slide c1 r1" viewBox="0 0 520 293">
  <polygon points="160,0 520,0 520,293 230,293 370,165" fill="var(--sky)"/>
  <polygon points="160,0 250,0 205,38" fill="var(--navy)"/>
  <polygon points="300,0 520,0 520,80 400,80" fill="var(--blue)" opacity=".6"/>
  <polygon points="370,165 520,293 230,293" fill="var(--blue)" opacity=".7"/>
  <text x="30" y="125" font-size="27" font-weight="700" fill="var(--blue)">PRESENTATION</text>
  <text x="30" y="153" font-size="25" fill="var(--blue)">TEMPLATE</text>
  <rect x="78" y="188" width="28" height="28" fill="var(--blue)"/>
  <text x="92" y="245" text-anchor="middle" font-size="17" font-weight="700" fill="var(--blue)">BRANNOW</text>
  <text x="92" y="258" text-anchor="middle" font-size="7" font-weight="700" fill="var(--blue)" letter-spacing="2">ADVISORY</text>
  <text x="450" y="44" class="brand-w">BRANNOW</text>
</svg>

<!-- Process steps -->
<svg class="slide c2 r1" viewBox="0 0 520 293">
  <defs><linearGradient id="hdr" x1="0" x2="1"><stop offset="0" stop-color="var(--deep)"/><stop offset="1" stop-color="var(--sky)"/></linearGradient></defs>
  <rect width="520" height="110" fill="url(#hdr)"/>
  <polygon points="260,0 520,0 520,110 330,110" fill="var(--blue)" opacity=".5"/>
  <text x="20" y="35" class="title-w"><tspan class="b">Lorem</tspan> ipsum dolor <tspan class="b">sit amet,</tspan> consectetur</text>
  <text x="20" y="55" class="title-w"><tspan class="b">adipiscing</tspan> elit.</text>
  <g fill="none" stroke="var(--grey)" stroke-width="1">
    <path d="M52 155H100L140 210H145M140 206l5 4-5 4"/>
    <path d="M163 155H211L251 210H256M251 206l5 4-5 4"/>
    <path d="M274 155H322L362 210H367M362 206l5 4-5 4"/>
    <path d="M384 155H432L472 210H477M472 206l5 4-5 4"/>
  </g>
  <g fill="var(--deep)"><circle cx="52" cy="155" r="8"/><circle cx="163" cy="155" r="8"/><circle cx="274" cy="155" r="8"/><circle cx="384" cy="155" r="8"/></g>
  <g fill="#fff"><path d="M49 151l7 4-7 4z"/><path d="M160 151l7 4-7 4z"/><path d="M271 151l7 4-7 4z"/><path d="M381 151l7 4-7 4z"/></g>
  <text x="54" y="190" class="num">01</text><text x="165" y="190" class="num">02</text><text x="276" y="190" class="num">03</text><text x="386" y="190" class="num">04</text>
  <text x="44" y="210" class="lab">Lorem ipsum</text><text x="155" y="210" class="lab">Lorem ipsum</text><text x="266" y="210" class="lab">Lorem ipsum</text><text x="376" y="210" class="lab">Lorem ipsum</text>
  <text x="44" y="220" class="fine">Lorem ipsum dolor sit amet</text><text x="155" y="220" class="fine">Lorem ipsum dolor sit amet</text><text x="266" y="220" class="fine">Lorem ipsum dolor sit amet</text><text x="376" y="220" class="fine">Lorem ipsum dolor sit amet</text>
  <text x="20" y="278" class="foot">2019 Business Corporation</text><text x="492" y="272" class="foot">01</text>
</svg>

<!-- Rating cards -->
<svg class="slide c3 r1" viewBox="0 0 520 293">
  <text x="20" y="35" class="title"><tspan class="b">Lorem</tspan> ipsum dolor <tspan class="b">sit amet,</tspan> consectetur</text>
  <text x="20" y="55" class="title"><tspan class="b">adipiscing</tspan> elit.</text>
  <rect x="438" y="30" width="8" height="8" fill="var(--blue)"/><text x="450" y="38" class="brand">BRANNOW</text>
  <g>
    <rect x="42" y="95" width="95" height="145" rx="8" fill="var(--mist)"/>
    <rect x="155" y="95" width="95" height="145" rx="8" fill="var(--mist)"/>
    <rect x="268" y="95" width="95" height="145" rx="8" fill="var(--mist)"/>
    <rect x="381" y="95" width="95" height="145" rx="8" fill="var(--mist)"/>
    <rect x="42" y="105" width="88" height="35" rx="6" fill="var(--blue)"/>
    <rect x="155" y="105" width="88" height="35" rx="6" fill="var(--deep)"/>
    <rect x="268" y="105" width="88" height="35" rx="6" fill="var(--blue)"/>
    <rect x="381" y="105" width="88" height="35" rx="6" fill="var(--deep)"/>
  </g>
  <g fill="#fff" font-size="9"><text x="52" y="127">01</text><text x="165" y="127">02</text><text x="278" y="127">03</text><text x="391" y="127">04</text></g>
  <g fill="none" stroke="#fff" stroke-width="1.5">
    <circle cx="102" cy="118" r="5"/><path d="M93 133q9-14 18 0"/>
    <circle cx="215" cy="118" r="5"/><path d="M206 133q9-14 18 0"/>
    <circle cx="328" cy="118" r="5"/><path d="M319 133q9-14 18 0"/>
    <circle cx="441" cy="118" r="5"/><path d="M432 133q9-14 18 0"/>
  </g>
  <text x="52" y="158" class="lab">Lorem ipsum</text><text x="165" y="158" class="lab">Lorem ipsum</text><text x="278" y="158" class="lab">Lorem ipsum</text><text x="391" y="158" class="lab">Lorem ipsum</text>
  <text x="52" y="170" class="fine">Lorem ipsum dolor sit amet</text><text x="165" y="170" class="fine">Lorem ipsum dolor sit amet</text><text x="278" y="170" class="fine">Lorem ipsum dolor sit amet</text><text x="391" y="170" class="fine">Lorem ipsum dolor sit amet</text>
  <g font-size="11" fill="var(--blue)"><text x="52" y="228">★★<tspan fill="#c8c8c8">★★★</tspan></text><text x="165" y="228">★★★<tspan fill="#c8c8c8">★★</tspan></text><text x="278" y="228">★★★★<tspan fill="#c8c8c8">★</tspan></text><text x="391" y="228">★★★★<tspan fill="#c8c8c8">★</tspan></text></g>
  <text x="20" y="278" class="foot">2019 Business Corporation</text><text x="492" y="272" class="foot">02</text>
</svg>

<!-- Timeline staircase -->
<svg class="slide c4 r1" viewBox="0 0 520 293">
  <text x="20" y="35" class="title"><tspan class="b">Lorem</tspan> ipsum dolor <tspan class="b">sit amet,</tspan> consectetur</text>
  <text x="20" y="55" class="title"><tspan class="b">adipiscing</tspan> elit.</text>
  <g fill="var(--mist)"><rect x="42" y="142" width="108" height="90"/><rect x="152" y="122" width="108" height="110"/><rect x="262" y="104" width="108" height="128"/><rect x="372" y="86" width="108" height="146"/></g>
  <g fill="var(--navy)"><rect x="42" y="142" width="108" height="16"/><rect x="152" y="122" width="108" height="16"/><rect x="262" y="104" width="108" height="16"/><rect x="372" y="86" width="108" height="16"/></g>
  <g fill="var(--blue)"><rect x="42" y="158" width="108" height="24"/><rect x="152" y="138" width="108" height="24"/><rect x="262" y="120" width="108" height="24"/><rect x="372" y="102" width="108" height="24"/></g>
  <g fill="#fff" font-size="8"><text x="48" y="153">2021</text><text x="158" y="133">2022</text><text x="268" y="115">2023</text><text x="378" y="97">2024</text></g>
  <g fill="#fff"><rect x="60" y="164" width="14" height="10"/><path d="M171 150l8-7 8 7v8h-16z"/><rect x="282" y="126" width="14" height="12"/><rect x="392" y="110" width="12" height="10"/></g>
  <g class="lab-w" font-size="6"><text x="80" y="173" class="lab-w">Lorem ipsum</text><text x="190" y="153" class="lab-w">Lorem ipsum</text><text x="302" y="135" class="lab-w">Lorem ipsum</text><text x="410" y="117" class="lab-w">Lorem ipsum</text></g>
  <text x="52" y="197" class="fine">Lorem ipsum dolor sit amet</text><text x="162" y="177" class="fine">Lorem ipsum dolor sit amet</text><text x="272" y="159" class="fine">Lorem ipsum dolor sit amet</text><text x="382" y="141" class="fine">Lorem ipsum dolor sit amet</text>
  <text x="20" y="278" class="foot">2019 Business Corporation</text><text x="492" y="272" class="foot">03</text>
</svg>

<!-- Hexagon steps -->
<svg class="slide c1 r2" viewBox="0 0 520 293">
  <text x="20" y="35" class="title"><tspan class="b">Lorem</tspan> ipsum dolor <tspan class="b">sit amet,</tspan> consectetur</text>
  <text x="20" y="55" class="title"><tspan class="b">adipiscing</tspan> elit.</text>
  <rect x="438" y="30" width="8" height="8" fill="var(--blue)"/><text x="450" y="38" class="brand">BRANNOW</text>
  <line x1="40" y1="110" x2="475" y2="110" stroke="var(--grey)"/>
  <g stroke="var(--navy)" stroke-width="3" fill="var(--blue)">
    <polygon points="76,110 87,91 109,91 120,110 109,129 87,129"/>
    <polygon points="177,110 188,91 210,91 221,110 210,129 188,129"/>
    <polygon points="279,110 290,91 312,91 323,110 312,129 290,129"/>
    <polygon points="381,110 392,91 414,91 425,110 414,129 392,129"/>
  </g>
  <g fill="#fff" stroke="#fff" stroke-width="2">
    <rect x="93" y="108" width="10" height="8" stroke="none"/><path d="M95 108v-3a3 3 0 0 1 6 0v3" fill="none"/>
    <circle cx="201" cy="108" r="5" fill="none"/><path d="M197 112l-5 5"/>
    <path d="M294 104l14 14M308 104l-14 14" fill="none"/>
    <circle cx="403" cy="110" r="8" stroke="none"/>
  </g>
  <text x="403" y="114" text-anchor="middle" font-size="11" font-weight="700" fill="var(--blue)">$</text>
  <g stroke="var(--grey)" stroke-dasharray="2 2"><line x1="98" y1="129" x2="98" y2="172"/><line x1="199" y1="129" x2="199" y2="172"/><line x1="301" y1="129" x2="301" y2="172"/><line x1="403" y1="129" x2="403" y2="172"/></g>
  <g fill="var(--mist)"><rect x="56" y="175" width="84" height="63"/><rect x="157" y="175" width="84" height="63"/><rect x="259" y="175" width="84" height="63"/><rect x="361" y="175" width="84" height="63"/></g>
  <g fill="var(--blue)"><circle cx="98" cy="173" r="6"/><circle cx="199" cy="173" r="6"/><circle cx="301" cy="173" r="6"/><circle cx="403" cy="173" r="6"/></g>
  <g fill="#fff" font-size="5" text-anchor="middle"><text x="98" y="175">01</text><text x="199" y="175">02</text><text x="301" y="175">03</text><text x="403" y="175">04</text></g>
  <g text-anchor="middle"><text x="98" y="200" class="lab">Lorem ipsum</text><text x="199" y="200" class="lab">Lorem ipsum</text><text x="301" y="200" class="lab">Lorem ipsum</text><text x="403" y="200" class="lab">Lorem ipsum</text>
  <text x="98" y="212" class="fine">Lorem ipsum dolor sit amet</text><text x="199" y="212" class="fine">Lorem ipsum dolor sit amet</text><text x="301" y="212" class="fine">Lorem ipsum dolor sit amet</text><text x="403" y="212" class="fine">Lorem ipsum dolor sit amet</text></g>
  <text x="20" y="278" class="foot">2019 Business Corporation</text><text x="492" y="272" class="foot">04</text>
</svg>

<!-- Chart -->
<svg class="slide c2 r2" viewBox="0 0 520 293">
  <text x="20" y="35" class="title"><tspan class="b">Lorem</tspan> ipsum dolor <tspan class="b">sit amet,</tspan> consectetur</text>
  <text x="20" y="55" class="title"><tspan class="b">adipiscing</tspan> elit.</text>
  <rect x="438" y="30" width="8" height="8" fill="var(--blue)"/><text x="450" y="38" class="brand">BRANNOW</text>
  <g font-size="5" fill="var(--grey)"><text x="44" y="98">100</text><text x="46" y="133">80</text><text x="46" y="168">60</text><text x="46" y="202">40</text><text x="46" y="237">20</text></g>
  <line x1="58" y1="235" x2="318" y2="235" stroke="#ccc"/>
  <g fill="#ececec"><rect x="72" y="182" width="18" height="53"/><rect x="123" y="190" width="18" height="45"/><rect x="174" y="150" width="18" height="85"/><rect x="225" y="120" width="18" height="115"/><rect x="276" y="140" width="18" height="95"/></g>
  <polyline points="81,170 132,175 183,137 234,108 285,127 315,127" fill="none" stroke="var(--grey)"/>
  <g fill="var(--blue)"><circle cx="81" cy="170" r="7"/><circle cx="132" cy="175" r="7"/><circle cx="183" cy="137" r="7"/><circle cx="234" cy="108" r="7"/>
  <circle cx="81" cy="235" r="2"/><circle cx="132" cy="235" r="2"/><circle cx="183" cy="235" r="2"/><circle cx="234" cy="235" r="2"/><circle cx="285" cy="235" r="2"/></g>
  <g fill="#fff" font-size="4.5" text-anchor="middle"><text x="81" y="172">55%</text><text x="132" y="177">43%</text><text x="183" y="139">71%</text><text x="234" y="110">83%</text></g>
  <g font-size="5" fill="var(--ink)" text-anchor="middle"><text x="81" y="244">Lorem ipsum</text><text x="132" y="244">Lorem ipsum</text><text x="183" y="244">Lorem ipsum</text><text x="234" y="244">Lorem ipsum</text><text x="285" y="244">Lorem ipsum</text></g>
  <g fill="var(--blue)"><circle cx="378" cy="100" r="8"/><circle cx="378" cy="133" r="8"/><circle cx="378" cy="165" r="8"/><circle cx="378" cy="198" r="8"/><circle cx="378" cy="231" r="8"/></g>
  <g fill="#fff" font-size="4.5" text-anchor="middle"><text x="378" y="102">55%</text><text x="378" y="135">43%</text><text x="378" y="167">71%</text><text x="378" y="200">83%</text><text x="378" y="233">72%</text></g>
  <text x="396" y="96" class="lab">Lorem ipsum</text><text x="396" y="129" class="lab">Lorem ipsum</text><text x="396" y="161" class="lab">Lorem ipsum</text><text x="396" y="194" class="lab">Lorem ipsum</text><text x="396" y="227" class="lab">Lorem ipsum</text>
  <text x="396" y="106" class="fine">Lorem ipsum dolor sit amet</text><text x="396" y="139" class="fine">Lorem ipsum dolor sit amet</text><text x="396" y="171" class="fine">Lorem ipsum dolor sit amet</text><text x="396" y="204" class="fine">Lorem ipsum dolor sit amet</text><text x="396" y="237" class="fine">Lorem ipsum dolor sit amet</text>
  <text x="20" y="278" class="foot">2019 Business Corporation</text><text x="492" y="272" class="foot">05</text>
</svg>

<!-- Section divider -->
<svg class="slide c3 r2" viewBox="0 0 520 293">
  <defs><linearGradient id="city" x1="0" x2="1" y1="0" y2="1"><stop offset="0" stop-color="#3a3d42"/><stop offset="1" stop-color="#111316"/></linearGradient></defs>
  <rect width="520" height="293" fill="url(#city)" role="img" aria-label="Night city skyline photograph"/>
  <polygon points="0,0 160,0 370,170 210,293 0,293" fill="var(--blue)" opacity=".92"/>
  <polygon points="160,0 290,0 370,170" fill="var(--navy)" opacity=".85"/>
  <text x="20" y="150" font-size="24" fill="#fff">Lorem ipsum dolor sit</text>
  <text x="20" y="183" font-size="24" fill="#fff">amet, consectetur</text>
  <text x="20" y="216" font-size="24" fill="#fff">adipiscing elit.</text>
  <text x="20" y="278" class="foot-w">2019 Business Corporation</text><text x="492" y="275" class="foot-w">06</text>
</svg>

<!-- Donuts -->
<svg class="slide c4 r2" viewBox="0 0 520 293">
  <text x="20" y="35" class="title"><tspan class="b">Lorem</tspan> ipsum dolor <tspan class="b">sit amet,</tspan> consectetur</text>
  <text x="20" y="55" class="title"><tspan class="b">adipiscing</tspan> elit.</text>
  <rect x="438" y="30" width="8" height="8" fill="var(--blue)"/><text x="450" y="38" class="brand">BRANNOW</text>
  <g fill="none">
    <circle cx="104" cy="150" r="38" stroke="#3a3d42" stroke-width="10"/>
    <circle cx="264" cy="150" r="38" stroke="#3a3d42" stroke-width="10"/>
    <circle cx="424" cy="150" r="38" stroke="#3a3d42" stroke-width="10"/>
    <circle cx="264" cy="150" r="38" stroke="#cfd0d2" stroke-width="10" stroke-dasharray="72 167" transform="rotate(-90 264 150)"/>
    <circle cx="424" cy="150" r="38" stroke="#cfd0d2" stroke-width="10" stroke-dasharray="86 153" transform="rotate(-90 424 150)"/>
    <circle cx="104" cy="150" r="46" stroke="var(--blue)" stroke-width="4" stroke-dasharray="42 247" transform="rotate(-90 104 150)"/>
    <circle cx="264" cy="150" r="46" stroke="var(--blue)" stroke-width="4" stroke-dasharray="87 202" transform="rotate(-90 264 150)"/>
    <circle cx="424" cy="150" r="46" stroke="var(--blue)" stroke-width="4" stroke-dasharray="104 185" transform="rotate(-90 424 150)"/>
  </g>
  <g font-size="15" fill="var(--ink)" text-anchor="middle"><text x="104" y="156">15%</text><text x="264" y="156">30%</text><text x="424" y="156">36%</text></g>
  <g font-size="5" fill="var(--ink)"><text x="124" y="97">15%</text><text x="305" y="108">30%</text><text x="472" y="125">36%</text></g>
  <g stroke="var(--grey)" stroke-dasharray="2 2"><line x1="180" y1="95" x2="180" y2="205"/><line x1="342" y1="95" x2="342" y2="205"/></g>
  <text x="56" y="220" class="lab">Lorem ipsum</text><text x="216" y="220" class="lab">Lorem ipsum</text><text x="375" y="220" class="lab">Lorem ipsum</text>
  <text x="56" y="230" class="fine">Lorem ipsum dolor sit amet</text><text x="216" y="230" class="fine">Lorem ipsum dolor sit amet</text><text x="375" y="230" class="fine">Lorem ipsum dolor sit amet</text>
  <text x="20" y="278" class="foot">2019 Business Corporation</text><text x="492" y="272" class="foot">07</text>
</svg>

<!-- Pricing -->
<svg class="slide c1 r3" viewBox="0 0 520 293">
  <text x="20" y="35" class="title"><tspan class="b">Lorem</tspan> ipsum dolor <tspan class="b">sit amet,</tspan> consectetur</text>
  <text x="20" y="55" class="title"><tspan class="b">adipiscing</tspan> elit.</text>
  <rect x="438" y="44" width="8" height="8" fill="var(--blue)"/><text x="450" y="52" class="brand">BRANNOW</text>
  <g fill="var(--mist)"><rect x="42" y="90" width="102" height="147"/><rect x="155" y="90" width="102" height="147"/><rect x="266" y="90" width="102" height="147"/><rect x="376" y="90" width="102" height="147"/></g>
  <g><rect x="42" y="90" width="102" height="24" fill="var(--blue)"/><rect x="155" y="90" width="102" height="24" fill="var(--navy)"/><rect x="266" y="90" width="102" height="24" fill="var(--blue)"/><rect x="376" y="90" width="102" height="24" fill="var(--navy)"/>
  <rect x="42" y="205" width="102" height="32" fill="var(--blue)"/><rect x="155" y="205" width="102" height="32" fill="var(--navy)"/><rect x="266" y="205" width="102" height="32" fill="var(--blue)"/><rect x="376" y="205" width="102" height="32" fill="var(--navy)"/></g>
  <g fill="#fff" font-size="8"><text x="55" y="106">Price <tspan font-size="10">1</tspan></text><text x="165" y="106">Price <tspan font-size="10">2</tspan></text><text x="276" y="106">Price <tspan font-size="10">3</tspan></text><text x="387" y="106">Price <tspan font-size="10">4</tspan></text></g>
  <g font-size="26" fill="var(--ink)"><text x="58" y="150"><tspan font-size="11" dy="-12">$</tspan><tspan dy="12">299</tspan><tspan font-size="7">/M</tspan></text><text x="170" y="150"><tspan font-size="11" dy="-12">$</tspan><tspan dy="12">399</tspan><tspan font-size="7">/M</tspan></text><text x="281" y="150"><tspan font-size="11" dy="-12">$</tspan><tspan dy="12">499</tspan><tspan font-size="7">/M</tspan></text><text x="393" y="150"><tspan font-size="11" dy="-12">$</tspan><tspan dy="12">599</tspan><tspan font-size="7">/M</tspan></text></g>
  <text x="55" y="172" class="lab">Lorem ipsum</text><text x="165" y="172" class="lab">Lorem ipsum</text><text x="276" y="172" class="lab">Lorem ipsum</text><text x="386" y="172" class="lab">Lorem ipsum</text>
  <text x="55" y="183" class="fine">Lorem ipsum dolor sit amet</text><text x="165" y="183" class="fine">Lorem ipsum dolor sit amet</text><text x="276" y="183" class="fine">Lorem ipsum dolor sit amet</text><text x="386" y="183" class="fine">Lorem ipsum dolor sit amet</text>
  <g fill="#fff"><rect x="60" y="213" width="66" height="15"/><rect x="180" y="213" width="52" height="15"/><rect x="291" y="213" width="52" height="15"/><rect x="401" y="213" width="52" height="15"/></g>
  <g font-size="8" fill="var(--ink)" text-anchor="middle"><text x="93" y="223">Promotion</text><text x="206" y="223">Buy</text><text x="317" y="223">Buy</text><text x="427" y="223">Buy</text></g>
  <text x="20" y="278" class="foot">2019 Business Corporation</text><text x="492" y="272" class="foot">08</text>
</svg>

<!-- Feature arrows -->
<svg class="slide c2 r3" viewBox="0 0 520 293">
  <text x="20" y="35" class="title"><tspan class="b">Lorem</tspan> ipsum dolor <tspan class="b">sit amet,</tspan> consectetur</text>
  <text x="20" y="55" class="title"><tspan class="b">adipiscing</tspan> elit.</text>
  <rect x="446" y="44" width="8" height="8" fill="var(--blue)"/><text x="458" y="52" class="brand">BRANNOW</text>
  <g fill="none" stroke="var(--grey)" stroke-width="1.2">
    <path d="M100 102H228L238 130L228 158H100"/><path d="M342 102H470L480 130L470 158H342"/>
    <path d="M100 180H228L238 208L228 236H100"/><path d="M338 180H466L476 208L466 236H338"/>
  </g>
  <g><path d="M50 100H100L110 130L100 160H50a8 8 0 0 1-8-8V108a8 8 0 0 1 8-8z" fill="var(--blue)"/>
  <path d="M293 100H343L353 130L343 160H293a8 8 0 0 1-8-8V108a8 8 0 0 1 8-8z" fill="var(--navy)"/>
  <path d="M50 178H100L110 208L100 238H50a8 8 0 0 1-8-8V186a8 8 0 0 1 8-8z" fill="var(--navy)"/>
  <path d="M290 178H340L350 208L340 238H290a8 8 0 0 1-8-8V186a8 8 0 0 1 8-8z" fill="var(--blue)"/></g>
  <g fill="none" stroke="#fff" stroke-width="2.5">
    <rect x="62" y="120" width="28" height="20"/><path d="M62 120l14 11 14-11"/>
    <circle cx="322" cy="126" r="9"/><path d="M315 133l-9 9"/>
    <path d="M69 203v-6a7 7 0 0 1 14 0"/>
    <path d="M306 204h8l14-9v26l-14-9h-8z"/>
  </g>
  <rect x="64" y="203" width="22" height="18" fill="#fff"/>
  <text x="130" y="122" class="lab">Lorem ipsum</text><text x="372" y="122" class="lab">Lorem ipsum</text><text x="130" y="200" class="lab">Lorem ipsum</text><text x="366" y="200" class="lab">Lorem ipsum</text>
  <text x="130" y="134" class="fine">Lorem ipsum dolor sit amet</text><text x="372" y="134" class="fine">Lorem ipsum dolor sit amet</text><text x="130" y="212" class="fine">Lorem ipsum dolor sit amet</text><text x="366" y="212" class="fine">Lorem ipsum dolor sit amet</text>
  <text x="20" y="278" class="foot">2019 Business Corporation</text><text x="492" y="272" class="foot">09</text>
</svg>

<!-- Monitor -->
<svg class="slide c3 r3" viewBox="0 0 520 293">
  <text x="20" y="35" class="title"><tspan class="b">Lorem</tspan> ipsum dolor <tspan class="b">sit amet,</tspan> consectetur</text>
  <text x="20" y="55" class="title"><tspan class="b">adipiscing</tspan> elit.</text>
  <rect x="158" y="88" width="212" height="150" fill="#3a3d42" role="img" aria-label="Computer monitor illustration with a world map and ring chart on screen"/>
  <g stroke="var(--grey)" fill="none"><path d="M300 103H402M300 133H402M300 160H402M300 190H402"/><path d="M40 135H180"/></g>
  <g fill="var(--blue)"><circle cx="50" cy="155" r="7"/><circle cx="410" cy="103" r="7"/><circle cx="410" cy="133" r="7"/><circle cx="410" cy="160" r="7"/><circle cx="410" cy="190" r="7"/></g>
  <g fill="#fff" font-size="4" text-anchor="middle"><text x="50" y="157">12%</text><text x="410" y="105">12%</text><text x="410" y="135">12%</text><text x="410" y="162">12%</text><text x="410" y="192">12%</text></g>
  <text x="62" y="150" class="lab">Lorem ipsum</text><text x="62" y="160" class="fine">Lorem ipsum dolor sit amet</text>
  <text x="422" y="100" class="lab">Lorem ipsum</text><text x="422" y="130" class="lab">Lorem ipsum</text><text x="422" y="157" class="lab">Lorem ipsum</text><text x="422" y="187" class="lab">Lorem ipsum</text>
  <text x="422" y="110" class="fine">Lorem ipsum dolor sit amet</text><text x="422" y="140" class="fine">Lorem ipsum dolor sit amet</text><text x="422" y="167" class="fine">Lorem ipsum dolor sit amet</text><text x="422" y="197" class="fine">Lorem ipsum dolor sit amet</text>
  <rect x="430" y="258" width="8" height="8" fill="var(--blue)"/><text x="442" y="266" class="brand">BRANNOW</text>
  <text x="20" y="278" class="foot">2019 Business Corporation</text><text x="496" y="272" class="foot">10</text>
</svg>

<!-- Blue list -->
<svg class="slide c4 r3" viewBox="0 0 520 293">
  <defs><linearGradient id="bl" x1="0" x2="1"><stop offset="0" stop-color="var(--deep)"/><stop offset="1" stop-color="var(--sky)"/></linearGradient></defs>
  <rect width="520" height="293" fill="url(#bl)"/>
  <polygon points="170,0 300,0 480,170 330,293 200,293 350,170" fill="var(--blue)" opacity=".55"/>
  <polygon points="480,170 520,140 520,293 330,293" fill="#fff"/>
  <text x="20" y="35" class="title-w"><tspan class="b">Lorem</tspan> ipsum dolor <tspan class="b">sit amet,</tspan> consectetur</text>
  <text x="20" y="55" class="title-w"><tspan class="b">adipiscing</tspan> elit.</text>
  <g fill="#fff"><circle cx="58" cy="110" r="14"/><circle cx="58" cy="162" r="14"/><circle cx="58" cy="214" r="14"/></g>
  <g fill="var(--navy)"><path d="M51 110l7-6 7 6v7h-14z"/><rect x="52" y="158" width="12" height="9"/><rect x="52" y="208" width="12" height="11"/></g>
  <text x="88" y="96" class="lab-w">Lorem ipsum</text><text x="88" y="148" class="lab-w">Lorem ipsum</text><text x="88" y="200" class="lab-w">Lorem ipsum</text>
  <text x="88" y="107" class="fine-w">Lorem ipsum dolor sit amet</text><text x="88" y="159" class="fine-w">Lorem ipsum dolor sit amet</text><text x="88" y="211" class="fine-w">Lorem ipsum dolor sit amet</text>
  <rect x="430" y="258" width="8" height="8" fill="var(--blue)"/><text x="442" y="266" class="brand">BRANNOW</text>
  <text x="20" y="278" class="foot-w">2019 Business Corporation</text>
</svg>

<div class="copy headline">Sample layout of 12 pages</div>
<div class="copy note n1">Text and content can be modified later accoriding to your content</div>
<div class="copy note n2">Original vector and PPT files will be delivered once approved the design</div>
<div class="copy note n3">Will edit the content if u provide the details</div>

<div class="signoff">
  <div class="mark"></div>
  <div class="name">BRANNOW</div>
  <div class="sub">ADVISORY</div>
</div>
</body>
</html>
```